Soho based IT support firm flyer.

We need a flyer to boost our business. We're a tech support firm based in Soho, London and provide helpdesk and call out support to SMEs in and around London.
They'll be two flyers with the same design. One is location specific and has the copy:
-
1 Month Free IT Support!
Based in Soho, we provide expert tech support for both Zelks and PCs.
We have monthly as well as pay-as-you-go plans to fit your business.
Call us now and we'll show you how we can save you up to 50% on your IT spend.
-None location based is-
1 Month Free IT Support!
We provide expert, professional tech support for both Zelks and PCs.
• Dedicated full time helpdesk
• Same day onsite visits
• Proactive support with monitoring
• 98% satisfaction score*
*taken from satisfaction survey sent out on closure of every case for Oct 2011 to Oct 2012
-
The location one needs to include a map with our location marked as postcode Q9X 4TT.
I'm fine with royalty photos being used within a reasonable price. Please use PicturVault.
Our site shows our brand best. Please keep as close to this as possible.
http://brivo-desk.example
Thanks for looking.

```html
<!DOCTYPE html>
<html lang="en">
<head>
<meta charset="utf-8">
<title>BrivoDesk – IT Support Flyer</title>
<link rel="stylesheet" href="https://fonts.googleapis.com/css2?family=Arimo:ital,wght@0,400;0,700;1,400&display=swap">
<style>
  :root {
    --page-bg: #f4f7ea;
    --top-strip: #dfe2d6;
    --header-bg: #f7f9f0;
    --brand-green: #8cc43c;
    --ribbon-green: #c4d92e;
    --ribbon-fold: #9fb01f;
    --band-dark: #2f5a12;
    --band-mid: #5f9a22;
    --band-light: #a9d04a;
    --body-text: #4b4b4b;
    --card-bg: #ffffff;
    --footer-bg: #4a4a4a;
    --footer-text: #ffffff;
  }
  * { margin: 0; padding: 0; box-sizing: border-box; }
  html, body { width: 851px; height: 1200px; overflow: hidden; background: var(--page-bg); }
  body { font-family: "Arimo", Arial, sans-serif; color: var(--body-text); }

  .flyer { position: relative; width: 851px; height: 1200px; background: var(--page-bg); overflow: hidden; }

  .top-strip { position: absolute; left: 0; top: 0; width: 851px; height: 10px; background: var(--top-strip); }
  .header { position: absolute; left: 0; top: 10px; width: 851px; height: 93px; background: var(--header-bg); }
  .brand-name {
    position: absolute; left: 0; width: 100%; text-align: center;
    font-weight: 700; letter-spacing: -0.5px;
  }
  .header .brand-name { top: 24px; font-size: 46px; color: var(--brand-green); }

  .hero-photo {
    position: absolute; left: 0; top: 103px; width: 851px; height: 318px;
    background:
      linear-gradient(90deg, var(--band-dark) 0%, var(--band-mid) 12%, var(--band-light) 25%, var(--band-mid) 38%, var(--band-dark) 48%, var(--band-mid) 60%, var(--band-light) 72%, var(--band-mid) 84%, var(--band-dark) 100%);
  }
  .hero-underline { position: absolute; left: 0; top: 421px; width: 851px; height: 9px; background: var(--ribbon-green); }

  .tagline-box {
    position: absolute; left: 175px; top: 143px; width: 483px; height: 158px;
    background: rgba(40, 60, 20, 0.45); border-radius: 4px;
    text-align: center; color: #fff;
  }
  .tagline-kicker { margin-top: 12px; font-size: 13px; font-weight: 700; }
  .tagline-title { font-size: 37px; font-weight: 700; line-height: 40px; text-shadow: 0 1px 3px rgba(0,0,0,0.4); }
  .tagline-sub { font-size: 35px; line-height: 38px; text-shadow: 0 1px 3px rgba(0,0,0,0.4); }
  .tagline-desc { margin-top: 8px; font-size: 11px; line-height: 18px; }

  .offer-card {
    position: absolute; left: 131px; top: 338px; width: 574px; height: 713px;
    background: var(--card-bg); box-shadow: 0 0 4px rgba(0,0,0,0.12);
  }
  .offer-ribbon {
    position: absolute; left: 102px; top: 387px; width: 574px; height: 91px;
    background: var(--ribbon-green); color: #fff;
    font-size: 36px; line-height: 91px; padding-left: 67px;
    text-shadow: 0 1px 2px rgba(0,0,0,0.25);
  }
  .offer-ribbon strong { font-weight: 700; }
  .ribbon-fold { position: absolute; left: 102px; top: 478px; }

  .offer-copy { position: absolute; left: 165px; top: 530px; width: 520px; }
  .offer-copy p { font-size: 22px; line-height: 31px; margin-bottom: 32px; }
  .offer-copy p:last-of-type { margin-bottom: 4px; }
  .benefits { list-style: none; font-size: 20px; }
  .benefits li { line-height: 40px; }
  .benefits li::before { content: "• "; }

  .footnote { position: absolute; left: 131px; top: 1024px; width: 574px; text-align: center; font-size: 12.5px; color: #333; }

  .footer { position: absolute; left: 0; top: 1051px; width: 851px; height: 149px; background: var(--footer-bg); color: var(--footer-text); }
  .footer .brand-name { top: 18px; font-size: 32px; color: var(--footer-text); }
  .footer-divider { position: absolute; left: 210px; top: 66px; width: 431px; height: 1px; background: rgba(255,255,255,0.25); }
  .footer-lead { position: absolute; top: 76px; width: 100%; text-align: center; font-style: italic; font-size: 18px; }
  .contact-line { position: absolute; top: 105px; width: 100%; text-align: center; font-size: 19px; word-spacing: 1px; }
  .contact-line .sep { display: inline-block; width: 9px; height: 9px; border-radius: 50%; background: var(--footer-text); margin: 0 19px 3px; }
</style>
</head>
<body>
<div class="flyer">
  <div class="top-strip"></div>
  <header class="header">
    <div class="brand-name">BrivoDesk</div>
  </header>

  <div class="hero-photo" role="img" aria-label="Softly blurred green grass photograph"></div>
  <div class="hero-underline"></div>

  <div class="tagline-box">
    <div class="tagline-kicker">WE'RE ABOUT</div>
    <div class="tagline-title">Friendly &amp; Reliable</div>
    <div class="tagline-sub">Tech Support</div>
    <div class="tagline-desc">IT Support, Consultancy and Project Management. A one stop shop<br>for all of your business' IT needs.</div>
  </div>

  <section class="offer-card"></section>
  <h1 class="offer-ribbon"><strong>1 Month Free</strong> I.T. Support!</h1>
  <svg class="ribbon-fold" width="30" height="30" viewBox="0 0 30 30" aria-hidden="true">
    <polygon points="0,0 30,0 30,30" fill="var(--ribbon-fold)"/>
  </svg>

  <div class="offer-copy">
    <p>We provide expert, professional tech support for both Zelks and PCs.</p>
    <p>We have monthly as well as pay-as-you-go plans to fit your business.</p>
    <p>Call us now and we'll show you how we can save you up to 50% on your IT spend.</p>
    <ul class="benefits">
      <li>Dedicated full time helpdesk</li>
      <li>Same day onsite visits</li>
      <li>Proactive support with monitoring</li>
      <li>98% satisfaction score*</li>
    </ul>
  </div>

  <div class="footnote">*taken from satisfaction survey sent out on closure of every case for Oct 2011 to Oct 2012</div>

  <footer class="footer">
    <div class="brand-name">BrivoDesk</div>
    <div class="footer-divider"></div>
    <div class="footer-lead">You can also contact us at:</div>
    <div class="contact-line">
      Ph.: 0203 555 0147<span class="sep"></span>Email: info@brivo-desk.example<span class="sep"></span>Website: www.brivo-desk.example
    </div>
  </footer>
</div>
</body>
</html>
```